Solvane site with a story.

Hi!

This project is to create a website for a restaurant.

Inspiration you can get from
http://www.brevik-solhagen.com/catering/
http://www.kavu-restaurant.com/
http://www.tobelgrenrestaurant.se/fine-dining/
http://www.elcorsotaberna.com/lima/

I have written a pdf that is attached. Please read that for more info.

I would LOVE to have the website made witin parallax like this website: http://www.brevik-solhagen.com/se/

I have made a preliminary logotype and drawed some pictures, how it can look. Is an example- you maybe can improve it if you think its needed.

I will be available 24/7 from now for any question about project.
Updates

Reason: The project has been to a slow start, so I am increasing the deadline time of the project. Thanks

Reason: Hi! Site has been a bit slow unfortunately - I will do the following. I will scetch up a new descrition of project which will involve much less animation. will come back with this tomorrow.

Hi!

Please see descpriton

Hi Everybody!

I have decided to wait with the pictures (page 6 in pdf) and focus on these parts:

1) Create a website with inspiration from the two websites i wrote about in description
2) http://glimmerlund.tavbok.se/   I want to add bookingsystem like this. 
http://www.glimmerlund.com/  (click "Boka" to see it live).
3) A contact form for visitors to post message that is sent to me. (name, number, company, text)

The past animation/parallax is totally replaced by this.  And

Reason: Because I need time to organize your work. I have understood that you have difficulties to understand my idea or vision. I have to givemore information to you, and that's why I'm extending the time.

Target Market(s)

35+ people with intesting in fine bistro dining.

Industry/Entity Type

Restaurant

Requirements
Must have
• Nice design. See page 4 for example of artwork in photoshop needed.

Also system for booking a table, or booking catering also important
Should not have
• It should not relate to "cheap tex mex".

```html
<!DOCTYPE html>
<html lang="en">
<head>
<meta charset="utf-8">
<title>Solvane – Fine Bistro Dining</title>
<link rel="stylesheet" href="https://fonts.googleapis.com/css2?family=Pinyon+Script&family=Open+Sans:wght@400&display=swap">
<style>
  :root {
    --ink: #000000;
    --panel: rgba(4, 3, 2, 0.86);
    --panel-edge: rgba(120, 110, 100, 0.55);
    --brand-orange: #ec9822;
    --button-orange: #f49d20;
    --button-text: #3a2308;
    --nav-text: #f3efe8;
    --footer-bg: rgba(18, 16, 14, 0.9);
    --footer-text: #f5f5f5;
    --icon-grey: #8e8e8e;
    --arrow-bg: rgba(200, 200, 200, 0.45);
    --arrow-mark: #6f6f6f;
  }
  * { margin: 0; padding: 0; box-sizing: border-box; }
  html, body {
    width: 1200px;
    height: 802px;
    overflow: hidden;
    background: var(--ink);
  }
  .page {
    position: relative;
    width: 1200px;
    height: 802px;
    overflow: hidden;
  }
  .hero-photo {
    position: absolute;
    inset: 0;
    background:
      radial-gradient(ellipse 360px 220px at 1050px 120px, rgba(214, 190, 140, 0.85), transparent 70%),
      radial-gradient(ellipse 300px 200px at 720px 110px, rgba(190, 160, 105, 0.75), transparent 70%),
      radial-gradient(ellipse 260px 150px at 700px 330px, rgba(180, 150, 100, 0.6), transparent 70%),
      radial-gradient(ellipse 380px 200px at 860px 580px, rgba(225, 222, 212, 0.85), transparent 70%),
      radial-gradient(ellipse 230px 320px at 60px 200px, rgba(150, 140, 60, 0.6), transparent 70%),
      linear-gradient(180deg, #3a2a18 0%, #2a1c10 45%, #4a2c16 70%, #1a120a 100%);
  }
  .menu-panel {
    position: absolute;
    left: 241px;
    top: 0;
    width: 305px;
    height: 542px;
    background: var(--panel);
    border: 1px solid var(--panel-edge);
    border-top: none;
    text-align: center;
  }
  .brand-name {
    position: absolute;
    left: 0;
    right: 0;
    top: 86px;
    font-family: "Open Sans", Arial, sans-serif;
    font-size: 28px;
    font-weight: 400;
    letter-spacing: 1px;
    color: var(--brand-orange);
    line-height: 34px;
  }
  .main-nav {
    position: absolute;
    left: 0;
    right: 0;
    top: 147px;
    list-style: none;
  }
  .main-nav li {
    height: 36px;
    font-family: "Pinyon Script", cursive;
    font-size: 18px;
    line-height: 26px;
    color: var(--nav-text);
  }
  .book-button {
    position: absolute;
    left: 100px;
    top: 406px;
    width: 103px;
    height: 28px;
    border-radius: 3px;
    background: var(--button-orange);
    font-family: "Open Sans", Arial, sans-serif;
    font-size: 13.5px;
    line-height: 28px;
    color: var(--button-text);
  }
  .next-slide {
    position: absolute;
    left: 1126px;
    top: 290px;
    width: 51px;
    height: 51px;
  }
  .site-footer {
    position: absolute;
    left: 0;
    top: 738px;
    width: 1200px;
    height: 64px;
    background: var(--footer-bg);
  }
  .copyright {
    position: absolute;
    left: 240px;
    top: 25px;
    font-family: Arial, Helvetica, sans-serif;
    font-size: 9.5px;
    color: var(--footer-text);
  }
  .social-links {
    position: absolute;
    left: 887px;
    top: 26px;
    display: flex;
    gap: 5px;
  }
  .social-links span {
    width: 14px;
    height: 14px;
    border-radius: 50%;
    background: var(--icon-grey);
  }
</style>
</head>
<body>
  <div class="page">
    <div class="hero-photo" role="img" aria-label="Restaurant table photograph: plated fish in leaf wraps with onion rings, small brass bowls of pickles, a wine glass and bottle, lit glass-block window behind"></div>

    <nav class="menu-panel" aria-label="Main menu">
      <div class="brand-name">Solvane</div>
      <ul class="main-nav">
        <li>Our Story</li>
        <li>Food &amp; Beverage</li>
        <li>Find us</li>
        <li>Catering</li>
        <li>Careers</li>
        <li>Events</li>
        <li>Giftcards</li>
      </ul>
      <div class="book-button">Book A Table</div>
    </nav>

    <svg class="next-slide" viewBox="0 0 51 51" aria-label="Next slide">
      <circle cx="25.5" cy="25.5" r="25" fill="var(--arrow-bg)"/>
      <path d="M20 15 L31 25.5 L20 36" fill="none" stroke="var(--arrow-mark)" stroke-width="6" stroke-linecap="round" stroke-linejoin="round"/>
    </svg>

    <footer class="site-footer">
      <p class="copyright">Copyright ©2013. Solvane.com. All Rights Reserved.</p>
      <div class="social-links" aria-label="Social links">
        <span></span><span></span><span></span><span></span>
      </div>
    </footer>
  </div>
</body>
</html>
```